Responsive, beautiful email sign-up process pages

My client wants to re-imagine their email newsletter sign up process. The funnel currently starts in the first panel of their home page carousel at:

https://thriftbeacon.co.uk/

It is also featured in the right side of the footer.

I would like to start, what could become a full template re-design project by optimising this crucial user journey. I am attaching the screenshots from the current user journey below and it would be great to get some designs that improve on the look and feel.

Thank you,
Dorian

Target Market(s)

People who want to maximise the interest rate they receive on their cash savings.

Industry/Entity Type

Financial Service

Coding

Coded - Design and coding required

Number of Pages Required

4 page

Font styles to use
Sans Serif

Requirements
Must have
• A well designed, responsive design for all of the elements of the user journey funnel that works well on desktop, laptop, tablet and phone. The site is currently using Bootstrap 3.* for the responsive templates, so it would be useful to continue leveraging these libraries, but in a much more visually appealing way.
• It is felt that the current overall site is dull and unprofessional, so we are using this as a way of showing how much better it could be, which should lead to a sitewide "facelift".
Nice to have
• Creative use of css, svg and javascript to optimise the user experience on all target platforms.
Should not have
• Non-responsive designs.

```html
<!DOCTYPE html>
<html lang="en">
<head>
<meta charset="utf-8">
<title>Thrift Beacon – Savings Sign Up</title>
<link href="https://fonts.googleapis.com/css2?family=Open+Sans:wght@400;600;700&display=swap" rel="stylesheet">
<style>
:root{
  --orange:#f47b20;
  --orange-dark:#d9650f;
  --ink:#333;
  --muted:#777;
  --nav:#3f3f3f;
  --footer:#2f2f2f;
  --footer-base:#242424;
  --panel:#f2f2f2;
  --line:#dcdcdc;
  --white:#fff;
}
*{box-sizing:border-box;margin:0;padding:0}
html,body{width:870px;height:1200px;overflow:hidden}
body{font-family:"Open Sans",Arial,sans-serif;color:var(--ink);background:var(--white);position:relative;font-size:9px}
.site-header{height:42px;display:flex;align-items:center;justify-content:space-between;padding:0 40px}
.brand{display:flex;align-items:center;gap:6px;font-size:17px;font-weight:700;color:var(--ink)}
.brand-mark{width:14px;height:14px;background:var(--orange)}
.header-contact{display:flex;align-items:center;gap:14px}
.expert-line{text-align:left;line-height:1.3}
.expert-line strong{display:block;font-size:11px}
.header-btn{background:var(--nav);color:var(--white);padding:4px 9px;font-size:8px;font-weight:600}
.header-btn.alt{background:var(--orange)}
.main-nav{height:20px;background:var(--nav);display:flex;justify-content:center;align-items:center;gap:22px;color:#e8e8e8;font-size:8px}
.search-bar{height:26px;display:flex;align-items:center;justify-content:space-between;padding:0 40px;background:var(--white);border-bottom:1px solid var(--line)}
.search-bar .pitch{font-size:11px;font-weight:700}
.pitch em{font-style:normal;color:var(--orange)}
.search-form{display:flex;gap:4px}
.search-form span{width:110px;height:16px;border:1px solid var(--line);background:var(--white);font-size:7px;color:var(--muted);padding:3px 5px}
.search-form b{background:var(--orange);color:var(--white);font-size:8px;padding:3px 10px}
.hero{position:absolute;top:88px;left:0;width:870px;height:327px;background:linear-gradient(135deg,#a9c6d8 0%,#d7dfe2 35%,#b8c2a0 60%,#8c8f6a 100%)}
.signup-modal{position:absolute;top:145px;left:315px;width:230px;height:230px;background:var(--white);border:3px solid var(--orange);box-shadow:0 4px 14px rgba(0,0,0,.3);padding:12px 16px}
.signup-modal h2{font-size:13px;font-weight:700;margin-bottom:2px}
.signup-modal .sub{font-size:7px;color:var(--muted);margin-bottom:8px}
.ticks{list-style:none;margin-bottom:10px}
.ticks li{display:flex;align-items:center;gap:5px;font-size:7px;color:var(--muted);margin-bottom:3px}
.field{height:17px;border:1px solid var(--line);font-size:7px;color:#999;padding:4px 6px;margin-bottom:6px}
.continue{display:inline-block;margin:4px auto 0;background:var(--orange);color:var(--white);font-size:8px;font-weight:600;padding:4px 14px}
.modal-foot{text-align:center}
.chevron{position:absolute;top:445px;left:423px}
.section-title{position:absolute;left:0;width:870px;text-align:center;color:var(--orange);font-size:17px;font-weight:400}
.advice{position:absolute;top:530px;left:0;width:870px;height:180px;background:var(--panel)}
.advice-grid{position:absolute;top:552px;left:40px;width:790px;display:flex;gap:14px}
.advice-card{flex:1;background:var(--white);height:140px;padding:12px;text-align:center;display:flex;flex-direction:column;align-items:center}
.advice-card h3{font-size:14px;color:var(--orange);font-weight:600;margin-bottom:8px}
.advice-card p{font-size:7px;color:var(--muted);line-height:1.5;flex:1}
.more-btn{border:1px solid var(--line);color:var(--muted);font-size:7px;padding:3px 12px}
.press-grid{position:absolute;top:750px;left:40px;width:790px;display:flex;gap:14px}
.quote-card{flex:1;height:215px;border:1px solid var(--line);padding:12px;font-size:7.5px;line-height:1.6;color:var(--muted)}
.quote-card cite{display:block;margin-top:8px;font-style:normal;font-weight:700;color:var(--ink)}
.press-strip{position:absolute;top:985px;left:0;width:870px;height:62px;background:var(--panel);display:flex;align-items:center;justify-content:center;gap:10px}
.press-badge{width:80px;height:38px;background:#d4d4d4;border-radius:3px}
.queries{position:absolute;top:1060px;left:0;width:870px;text-align:center;font-size:19px;color:var(--orange)}
.site-footer{position:absolute;top:1100px;left:0;width:870px;height:78px;background:var(--footer);display:flex;gap:20px;padding:12px 40px;color:#bbb;font-size:7px;line-height:1.6}
.foot-col{flex:1}
.foot-col h4{color:var(--orange);font-size:8px;margin-bottom:3px}
.foot-signup span{display:block;height:14px;background:var(--white);margin-top:4px;width:150px}
.foot-signup b{display:inline-block;background:var(--orange);color:var(--white);padding:1px 8px;margin-top:4px}
.footer-base{position:absolute;top:1178px;left:0;width:870px;height:22px;background:var(--footer-base);color:#999;font-size:7px;padding:6px 40px;display:flex;gap:14px}
</style>
</head>
<body>
<header class="site-header">
  <div class="brand"><span class="brand-mark"></span>Thrift Beacon</div>
  <div class="header-contact">
    <div class="expert-line">Speak Direct to a Savings Expert<strong>0800 555 0142</strong></div>
    <span class="header-btn">Sign In</span>
    <span class="header-btn alt">Register Here</span>
  </div>
</header>
<nav class="main-nav">
  <span>Home</span><span>Best Buy Tables</span><span>Savings Help</span><span>Account Reviews</span><span>Rate Tracker</span><span>Premium</span><span>Testimonials</span><span>About Us</span><span>Contact</span>
</nav>
<div class="search-bar">
  <div class="pitch">Get <em>FREE</em> whole of market information</div>
  <div class="search-form"><span>Your name</span><span>Email address</span><b>Search</b></div>
</div>

<div class="hero" role="img" aria-label="Photo of a relaxed couple resting in a hammock outdoors"></div>

<div class="signup-modal">
  <h2>Next step of sign up</h2>
  <p class="sub">Tell us a bit more about you</p>
  <ul class="ticks">
    <li><svg width="8" height="8" viewBox="0 0 8 8"><path d="M1 4l2 2 4-5" stroke="#f47b20" stroke-width="1.5" fill="none"/></svg>Best rates sent to your inbox</li>
    <li><svg width="8" height="8" viewBox="0 0 8 8"><path d="M1 4l2 2 4-5" stroke="#f47b20" stroke-width="1.5" fill="none"/></svg>Alerts when your rate drops</li>
    <li><svg width="8" height="8" viewBox="0 0 8 8"><path d="M1 4l2 2 4-5" stroke="#f47b20" stroke-width="1.5" fill="none"/></svg>We never share your details</li>
  </ul>
  <div class="field">Your first name</div>
  <div class="field">Your last name</div>
  <div class="field">Password</div>
  <div class="modal-foot"><span class="continue">Continue ›</span></div>
</div>

<svg class="chevron" width="24" height="14" viewBox="0 0 24 14"><path d="M2 2l10 9 10-9" stroke="#f47b20" stroke-width="3" fill="none"/></svg>

<h2 class="section-title" style="top:495px">Specialist Advice</h2>
<div class="advice"></div>
<div class="advice-grid">
  <div class="advice-card"><h3>£100,000 plus in savings?</h3><p>Our dedicated team can help you spread large sums across secure accounts, keep within protection limits and earn more interest.</p><span class="more-btn">Would you like to know more?</span></div>
  <div class="advice-card"><h3>Wealth Management</h3><p>We match you with trusted advisers for pensions, investments and longer term planning tailored to your goals.</p><span class="more-btn">Would you like to know more?</span></div>
  <div class="advice-card"><h3>Take Our £50 Challenge</h3><p>If we cannot find you at least fifty pounds more interest a year, we will tell you straight away and at no cost.</p><span class="more-btn">Would you like to know more?</span></div>
</div>

<h2 class="section-title" style="top:715px">Thrift Beacon in the Press</h2>
<div class="press-grid">
  <div class="quote-card">“Thrift Beacon is a treasure trove of facts for anyone who wants to keep track of their savings. Clear tables, honest guides and timely alerts make it one of the best free resources around for savers.”<cite>Lena Marlowe, Deputy Personal Finance Editor, Northgate Media Group</cite></div>
  <div class="quote-card">“Thrift Beacon is a great website for the serious saver: independent, unbiased and informative.”<cite>Owen Radley, Personal Finance Editor, Weekend Ledger</cite></div>
  <div class="quote-card">“You can check on cash interest rates on several websites, but the best has to be Thrift Beacon. Its clear layout and regular updates make comparing accounts quick, and its rate alerts help savers move their money at the right time.”<cite>Nina Carver, Coinwise Weekly</cite></div>
</div>

<div class="press-strip">
  <span class="press-badge"></span><span class="press-badge"></span><span class="press-badge"></span><span class="press-badge"></span><span class="press-badge"></span><span class="press-badge"></span><span class="press-badge"></span><span class="press-badge"></span><span class="press-badge"></span>
</div>

<p class="queries">Queries? Call us on 0800 555 0142</p>

<footer class="site-footer">
  <div class="foot-col"><h4>Are you looking for a better rate for your savings?</h4>Join thousands of savers who get our free rate updates every month.</div>
  <div class="foot-col"><h4>Savings Accounts</h4>Easy Access<br>Fixed Rate Bonds<br>Cash ISAs</div>
  <div class="foot-col"><h4>Helpful Links</h4>Rate Tracker<br>Savings Guides<br>Contact Us</div>
  <div class="foot-col foot-signup"><h4>Sign up for our newsletter</h4>Stay in the loop with the best rates.<span></span><b>Sign Up</b></div>
</footer>
<div class="footer-base"><span>Terms &amp; Conditions</span><span>Privacy Policy</span><span>Cookie Policy</span><span>Website Help</span></div>
</body>
</html>
```